We need a fresh, new church business card!!

We need a church business card with basic info to hand out as invites. We are looking for something clean that communicates our basic information clearly.

We are open to square or rectangle card sizes.

General Public

Religious

The attached logo is the only one that I have available. We'd like to see options with with text of the logo lighter and on a dark background as well as options with white/light backgrounds.

Also, we'd like to see option with rounded corners.

• Address - 2718 Maple Row, Rockford, IL 61142
• Website - brookvane.example
• Phone - 815-555-0163
• Service times -
• Sunday - 10am Sunday School
• - 11am Family Worship
• - 6pm Night of Prayer
• Wednesday - 7:30pm Adult Bible Study
• Classes for all ages

```html
<!DOCTYPE html>
<html lang="en">
<head>
<meta charset="utf-8">
<title>Brookvane Gospel Church – Business Card</title>
<link href="https://fonts.googleapis.com/css2?family=Cabin:wght@400;600;700&display=swap" rel="stylesheet">
<style>
  :root {
    --backdrop: #e9e7e3;
    --card-white: #ffffff;
    --card-black: #050505;
    --teal: #1d9aa6;
    --teal-deep: #168690;
    --silver: #9a9a9a;
    --shadow: rgba(0, 0, 0, 0.18);
  }
  * { box-sizing: border-box; margin: 0; padding: 0; }
  html, body {
    width: 1200px;
    height: 873px;
    overflow: hidden;
    background: var(--backdrop);
    font-family: "Cabin", Arial, sans-serif;
  }
  .canvas {
    position: relative;
    width: 1200px;
    height: 873px;
    display: flex;
    align-items: center;
    justify-content: center;
    gap: 60px;
  }
  .card {
    position: relative;
    width: 520px;
    height: 298px;
    border-radius: 22px;
    overflow: hidden;
    box-shadow: 0 10px 28px var(--shadow);
  }

  /* Front side */
  .card--front { background: var(--card-white); color: var(--teal); }
  .card--front .accent-end {
    position: absolute;
    right: 0; top: 0;
    width: 118px; height: 100%;
    background: var(--teal);
  }
  .contact {
    position: absolute;
    left: 34px; top: 30px;
    list-style: none;
    font-size: 17px;
    line-height: 1.45;
  }
  .contact li { display: flex; align-items: center; gap: 8px; }
  .contact svg { width: 13px; height: 13px; flex: none; fill: var(--teal); }
  .contact .web { padding-left: 21px; }
  .service-tab {
    position: absolute;
    left: 0; top: 124px;
    width: 168px; height: 34px;
    background: var(--teal);
    color: var(--card-white);
    font-size: 18px;
    line-height: 34px;
    padding-left: 34px;
    border-radius: 0 10px 10px 0;
  }
  .schedule {
    position: absolute;
    left: 34px; top: 176px;
    display: flex;
    gap: 34px;
    font-size: 14px;
    line-height: 1.4;
  }
  .schedule h3 {
    font-size: 14px;
    font-weight: 700;
    text-transform: uppercase;
    letter-spacing: 0.02em;
  }
  .schedule p { font-weight: 400; }

  /* Back side */
  .card--back { background: var(--card-black); }
  .card--back .accent-end {
    position: absolute;
    left: 0; top: 0;
    width: 118px; height: 100%;
    background: var(--teal);
  }
  .church-name {
    position: absolute;
    left: 150px; right: 30px; top: 0; bottom: 0;
    display: flex;
    align-items: center;
    justify-content: center;
    color: var(--silver);
    font-size: 30px;
    font-weight: 400;
    letter-spacing: 0.04em;
    text-transform: uppercase;
  }
</style>
</head>
<body>
<main class="canvas">

  <section class="card card--front" aria-label="Card front">
    <ul class="contact">
      <li>
        <svg viewBox="0 0 16 16" aria-hidden="true"><path d="M8 1 1 7.5h2V15h4v-4h2v4h4V7.5h2z"/></svg>
        2718 Maple Row, Rockford, IL 61142
      </li>
      <li>
        <svg viewBox="0 0 16 16" aria-hidden="true"><path d="M4 1h8a1 1 0 0 1 1 1v12a1 1 0 0 1-1 1H4a1 1 0 0 1-1-1V2a1 1 0 0 1 1-1zm1 2v9h6V3zm3 10.2a.8.8 0 1 0 0-1.6.8.8 0 0 0 0 1.6z"/></svg>
        815-555-0163
      </li>
      <li class="web">brookvane.example</li>
    </ul>

    <div class="service-tab">Service times</div>

    <div class="schedule">
      <div class="schedule__day">
        <h3>Sunday</h3>
        <p>10am Sunday School</p>
        <p>11am Family Worship</p>
        <p>6pm Night of Prayer</p>
      </div>
      <div class="schedule__day">
        <h3>Wednesday</h3>
        <p>7:30pm Adult Bible Study</p>
        <p>Classes for all ages</p>
      </div>
    </div>

    <div class="accent-end"></div>
  </section>

  <section class="card card--back" aria-label="Card back">
    <div class="accent-end"></div>
    <h1 class="church-name">Brookvane Gospel Church</h1>
  </section>

</main>
</body>
</html>
```